Water Filter Company Needs Bizz Cards!!

Need business cards for my company. We sell whole home water filters and salt free water softeners. No more buying bottled water. Our filtering units filter out all heavy metals, chlorine, and VOC's, last 15 years, and are maintenance free and supply your whole home with spring quality alkaline water. Our Salt free water conditioners, eliminate hard water and scale, without lowering the ph, or TDS's (total Dissolved solids)

I think this is the color code we are using on my site. My logo looks good behind it. #192841

Website will be www.Brevonix.com

Industry/Entity Type

Water Purification

Contact Information for Business Card

For now, just insert standard Dummy text. I need these text lines for the info to be editable so i can make them for multiple employees. I do have Photoshop and illustrator, unless there is a simpler program i can use solely for biz cards

Font styles to use
Sans Serif

Requirements
Must have
• Use my preexisting logo.

www.BrevoNix.com

Spring Quality Alkaline Water at every tap.

List out services. Whole Home Water Filters, Salt Free Water Softeners, Quendamar TX7, UV Sterilizers
Nice to have
• I think this is the color code we are using on my site. My logo looks good behind it. #192841 or black. Please no white or light blue backgrounds.

Maybe a picture of my tank.

Slogan like Spring Quality Alkaline Water at every tap.
And just list the services Whole Home Water Filters, Salt Free Water Softeners, Quendamar TX7, UV Sterilizers

I think I would like to not have a contrasting textured logo like I see on some of them. I may use it for my personal cards, but new employees may not want the extra expense.
Should not have
• A different logo than the one provided.

White or baby blue backgrounds. Use the color code, or blacks.

```html
<!DOCTYPE html>
<html lang="en">
<head>
<meta charset="utf-8">
<title>Brevonix Business Cards</title>
<link rel="stylesheet" href="https://fonts.googleapis.com/css2?family=Poppins:wght@600&family=Roboto+Condensed:wght@400;500&display=swap">
<style>
  :root {
    --page: #ecebe8;
    --card: #192841;
    --band: #33c2ef;
    --brand: #33c2ef;
    --ink: #ffffff;
    --muted: #b9c4d6;
    --tank-light: #e9e6c9;
    --tank-dark: #1c1c1c;
  }
  * { margin: 0; padding: 0; box-sizing: border-box; }
  html, body { width: 1200px; height: 750px; overflow: hidden; }
  body {
    background: var(--page);
    font-family: "Roboto Condensed", Arial, sans-serif;
    color: var(--ink);
    position: relative;
  }
  .card {
    position: absolute;
    width: 525px;
    height: 300px;
    background: var(--card);
    border-top: 9px solid var(--band);
    border-bottom: 9px solid var(--band);
    box-shadow: 0 14px 30px rgba(0,0,0,0.18);
  }
  .card--front { left: 45px; top: 225px; }
  .card--back { left: 630px; top: 225px; }

  .brand {
    display: flex;
    align-items: center;
    gap: 8px;
  }
  .brand__dot {
    width: 18px; height: 18px;
    border-radius: 50%;
    background: var(--brand);
  }
  .brand__name {
    font-family: "Poppins", Arial, sans-serif;
    font-weight: 600;
    color: var(--brand);
    letter-spacing: -0.5px;
    line-height: 1;
  }
  .card--front .front__stack {
    position: absolute;
    left: 0; right: 0; top: 50%;
    transform: translateY(-50%);
    display: flex;
    flex-direction: column;
    align-items: center;
    gap: 14px;
  }
  .card--front .brand__name { font-size: 50px; }
  .card--front .brand__dot { width: 30px; height: 30px; }
  .slogan {
    font-size: 14px;
    font-weight: 400;
    letter-spacing: 0.6px;
    color: var(--muted);
  }

  .card--back .brand { position: absolute; left: 30px; top: 26px; }
  .card--back .brand__name { font-size: 30px; }

  .tagline {
    position: absolute;
    left: 30px; top: 72px;
    font-size: 9px;
    font-weight: 500;
    letter-spacing: 0.2px;
    color: var(--muted);
  }
  .contact {
    position: absolute;
    left: 30px; top: 102px;
    list-style: none;
    font-size: 11.5px;
  }
  .contact li {
    display: flex;
    align-items: center;
    gap: 10px;
    height: 21px;
  }
  .contact svg { width: 12px; height: 12px; flex: none; }

  .services {
    position: absolute;
    right: 30px; top: 28px;
    list-style: none;
    text-align: right;
    font-size: 11px;
    font-weight: 500;
    line-height: 18px;
    letter-spacing: 0.3px;
  }
  .services li::before {
    content: "";
    display: inline-block;
    width: 5px; height: 5px;
    margin-right: 7px;
    vertical-align: middle;
    background: var(--band);
    border-radius: 50%;
  }

  .social {
    position: absolute;
    left: 158px; bottom: 14px;
    display: flex;
    gap: 8px;
  }
  .social span {
    width: 13px; height: 13px;
    background: var(--ink);
    border-radius: 2px;
  }
  .product {
    position: absolute;
    right: 60px; bottom: 20px;
    width: 150px; height: 120px;
    border-radius: 6px;
    background: linear-gradient(90deg, var(--tank-dark) 0%, #8a8a8a 45%, var(--tank-light) 75%, #d9d5b4 100%);
  }
</style>
</head>
<body>
  <section class="card card--front">
    <div class="front__stack">
      <div class="brand">
        <span class="brand__dot"></span>
        <span class="brand__name">Brevonix</span>
      </div>
      <p class="slogan">Spring Quality Alkaline Water at every tap.</p>
    </div>
  </section>

  <section class="card card--back">
    <div class="brand">
      <span class="brand__dot"></span>
      <span class="brand__name">Brevonix</span>
    </div>
    <p class="tagline">~ WHOLE HOME WATER FILTERS FOR THE BEST PRICE ~</p>
    <ul class="services">
      <li>Whole Home Water Filters</li>
      <li>Salt Free Water Softeners</li>
      <li>Quendamar TX7</li>
      <li>UV Sterilizers</li>
    </ul>
    <ul class="contact">
      <li>
        <svg viewBox="0 0 24 24"><path fill="#ffffff" d="M6.6 10.8a15 15 0 0 0 6.6 6.6l2.2-2.2c.3-.3.7-.4 1-.2 1.1.4 2.3.6 3.6.6.6 0 1 .4 1 1V20c0 .6-.4 1-1 1A17 17 0 0 1 3 4c0-.6.4-1 1-1h3.5c.6 0 1 .4 1 1 0 1.3.2 2.5.6 3.6.1.3 0 .7-.2 1z"/></svg>
        (55) 0198 342 610
      </li>
      <li>
        <svg viewBox="0 0 24 24"><path d="M2 5h20v14H2z" fill="none" stroke="#ffffff" stroke-width="2"/><path d="M2 5l10 8 10-8" fill="none" stroke="#ffffff" stroke-width="2"/></svg>
        HELLO@BREVONIX.COM
      </li>
      <li>
        <svg viewBox="0 0 24 24"><circle cx="12" cy="12" r="9" fill="none" stroke="#ffffff" stroke-width="2"/><path d="M3 12h18M12 3c3 3 3 15 0 18M12 3c-3 3-3 15 0 18" fill="none" stroke="#ffffff" stroke-width="1.6"/></svg>
        WWW.BREVONIX.COM
      </li>
      <li>
        <svg viewBox="0 0 24 24"><path fill="#ffffff" d="M12 2a7 7 0 0 0-7 7c0 5 7 13 7 13s7-8 7-13a7 7 0 0 0-7-7zm0 9.5A2.5 2.5 0 1 1 12 6.5a2.5 2.5 0 0 1 0 5z"/></svg>
        4827 ORCHARD LANE SPRINGFIELD, USA
      </li>
    </ul>
    <div class="product" role="img" aria-label="Product photo of whole home water filter tanks and a UV sterilizer"></div>
    <div class="social" aria-label="Social media links">
      <span></span><span></span><span></span><span></span>
    </div>
  </section>
</body>
</html>
```